Wordpress theme customised please - for new ecommerce homewares website

Hi, we need a wordpress theme customised for a business that will sell tea towels (aka kitchen towels/dish cloths).
We do not have a website currently, but wish to launch using wordpress + woocommerce + "the shopfront" theme (c/- plumkestrel).
BACKGROUND RE THE BUSINESS
Our products are very stylish and will appeal to people who like owning gorgeous things - people who love cooking and/or decorating their home beautifully, or maybe they like travelling and/or buying presents for themselves and friends/family etc.
As they are typically used in people's kitchens, so "fresh" and "clean" is important - however the site must look very upmarket: timeless yet current, and classic yet simple, but not pretty, fussy or edgy.
We believe we have a great opportunity to leverage the "feel" of the product - cotton & linen fabric that has real texture to it, is tactile, natural, raw, real... in the photos used on the website, the backgrounds etc
Our logo is attached - a very dark grey colour was chosen, with white stripes, so that its neutral colouring would coordinate well with our suppliers' existing packaging. (We will represent a number of brands.)
BACKGROUND RE THIS PROJECT
We already know we want to use "the shopfront" theme by plumkestrel, but we need help customising the look of this theme so it works well with our logo, looks really striking and doesn't look like everyone else's ie "straight out of the box".
It appears these are the types of things that can be changed:
LAYOUT:
home page design concept (eg with a cascade carousel)
page design concept for eg About Us, Contact Us, FAQs
landing page design concept
header; light footer; dark footer
COLOURS & BACKGROUNDS & BORDERS & SEPARATORS:
main theme colour; accent colour; primary font colour
header background; light footer background colour; dark footer background colour; copyright bar background colour
dark footer widget title border; dark footer list separators and borders; dark footer/copyright bar separator styles
FONTS:
main navigation text colour; secondary navigation text colour; dark footer text colour; copyright bar text colour
main font; secondary font
LASTLY
Please don't hesitate to ask questions, request further information etc This is the first time we've posted a design project like this so it's tricky to know what other information you will need, so please just get in touch, ok!
Thanks so much for your interest in this project, and best wishes.

```html
<!DOCTYPE html>
<html lang="en">
<head>
<meta charset="utf-8">
<title>Linen Larder – Home</title>
<link href="https://fonts.googleapis.com/css2?family=Playfair+Display:wght@700&family=Open+Sans:wght@400;600;700&family=Oswald:wght@400;500&display=swap" rel="stylesheet">
<style>
:root{
  --navy:#3e4f7f;
  --navy-light:#5a6c9c;
  --navy-dark:#2b3552;
  --navy-deeper:#222a41;
  --ink:#3b3f4a;
  --muted:#7a7f8a;
  --rule:#d9dce3;
  --paper:#ffffff;
  --mist:#f2f3f6;
}
*{box-sizing:border-box;margin:0;padding:0}
html,body{width:863px;height:1200px;overflow:hidden}
body{font-family:"Open Sans",Arial,sans-serif;color:var(--ink);background:var(--paper);position:relative}
.topbar{position:absolute;left:0;top:0;width:863px;height:22px;background:var(--mist);border-bottom:1px solid var(--rule);font-size:8px;color:var(--muted);display:flex;justify-content:space-between;align-items:center;padding:0 14px}
.topbar a{color:var(--navy);text-decoration:none}
.topbar .account-links span{margin-left:12px}
.site-header{position:absolute;top:22px;left:0;width:863px;height:80px;background:linear-gradient(#fafbfc,#eef0f4)}
.brand{position:absolute;top:16px;left:0;width:863px;text-align:center;font-family:"Playfair Display",Georgia,serif;font-weight:700;font-size:30px;letter-spacing:3px;color:var(--navy-dark)}
.main-nav{position:absolute;top:104px;left:115px;width:633px;height:28px;background:var(--navy);display:flex;padding-left:20px}
.main-nav a{color:#fff;font-family:"Oswald",sans-serif;font-size:11px;letter-spacing:.5px;text-decoration:none;padding:0 18px;line-height:28px}
.main-nav a.active{background:var(--navy-light)}
.hero{position:absolute;top:140px;left:112px;width:639px;height:248px;border:5px solid #e3e6ec;background:#fff}
.hero-image{position:absolute;inset:0;background:linear-gradient(100deg,#7fb7d6 0%,#d9dfe5 35%,#e8b35a 55%,#d64c4c 72%,#6fbf6a 100%)}
.hero-labels{position:absolute;left:0;right:0;bottom:34px;height:30px;background:rgba(255,255,255,.82);display:flex;justify-content:center;gap:34px;align-items:center}
.hero-labels span{font-size:13px;font-weight:700;color:var(--navy-dark)}
.hero-labels span::before{content:"✚ ";color:var(--navy)}
.hero-arrow{position:absolute;top:240px;width:22px;height:44px;background:var(--navy)}
.hero-arrow.prev{left:96px;border-radius:22px 0 0 22px}
.hero-arrow.next{left:749px;border-radius:0 22px 22px 0}
.hero-arrow svg{position:absolute;top:15px;left:6px}
.hero-dots{position:absolute;top:396px;left:0;width:863px;display:flex;justify-content:center;gap:5px}
.hero-dots i{width:6px;height:6px;border-radius:50%;background:#c7cbd4}
.hero-dots i.on{background:var(--navy)}
.section-title{position:absolute;left:115px;width:633px;display:flex;align-items:center;gap:12px;font-family:"Oswald",sans-serif;font-size:14px;letter-spacing:1px;color:var(--navy-dark)}
.section-title::before,.section-title::after{content:"";flex:1;height:1px;background:var(--rule)}
.featured-title{top:422px}
.category-list{position:absolute;top:458px;left:115px;width:318px}
.category{position:relative;height:72px;margin-bottom:8px}
.category .swatch{position:absolute;inset:0}
.category .label{position:absolute;left:60px;top:22px;height:28px;width:180px;background:#fff;color:var(--navy);font-family:"Oswald",sans-serif;font-size:14px;letter-spacing:.5px;line-height:28px;padding-left:18px}
.category .label svg{position:absolute;right:-14px;top:0}
.feature-image{position:absolute;top:458px;left:445px;width:303px;height:232px;background:linear-gradient(160deg,#e9eef2,#c9d6df 60%,#a9bccb)}
.welcome{position:absolute;top:720px;left:115px;width:390px}
.welcome h2,.testimonials h2{font-family:"Oswald",sans-serif;font-weight:500;font-size:13px;color:var(--navy-dark);padding-bottom:6px;border-bottom:1px solid var(--rule);margin-bottom:9px}
.welcome p{font-size:8px;line-height:1.55;color:var(--muted);margin-bottom:8px}
.btn{display:inline-block;background:var(--navy);color:#fff;font-size:8px;font-weight:700;padding:5px 12px;letter-spacing:.5px;text-decoration:none}
.testimonials{position:absolute;top:720px;left:525px;width:223px}
.quote{border:1px solid var(--rule);padding:10px 12px;font-size:8px;line-height:1.55;color:var(--muted);position:relative}
.quote::after{content:"";position:absolute;left:18px;bottom:-6px;width:10px;height:10px;background:#fff;border-right:1px solid var(--rule);border-bottom:1px solid var(--rule);transform:rotate(45deg)}
.author{display:flex;align-items:center;gap:8px;margin-top:12px;font-size:8px}
.author .avatar{width:26px;height:26px;border-radius:50%;background:#c9b8a6}
.author b{display:block;color:var(--navy-dark)}
.brands{position:absolute;top:912px;left:115px;width:633px;height:56px;border-top:1px solid var(--rule);border-bottom:1px solid var(--rule);display:flex;justify-content:space-around;align-items:center}
.brands span{font-size:14px;font-weight:700;color:var(--navy-dark);display:flex;align-items:center;gap:5px}
.brands span i{width:10px;height:10px;background:var(--navy);display:inline-block}
.site-footer{position:absolute;top:988px;left:0;width:863px;height:194px;background:var(--navy-dark);color:#c4c9d6}
.footer-cols{position:absolute;top:22px;left:115px;width:633px;display:flex;justify-content:space-between}
.footer-col{width:140px;font-size:8px;line-height:1.9}
.footer-col h3{font-family:"Oswald",sans-serif;font-weight:400;font-size:11px;color:#fff;border-bottom:1px solid #48557a;padding-bottom:4px;margin-bottom:5px}
.footer-col ul{list-style:none}
.footer-col li{display:flex;align-items:center;gap:5px;white-space:nowrap}
.footer-col .twin{display:flex;gap:18px}
.dot{width:9px;height:9px;border-radius:50%;background:#8f9ab6;display:inline-block}
.copyright{position:absolute;top:1182px;left:0;width:863px;height:18px;background:var(--navy-deeper);display:flex;justify-content:space-between;align-items:center;padding:0 115px;font-size:7px;color:#9aa3bb}
.copyright .mark{font-family:"Playfair Display",Georgia,serif;font-size:9px;letter-spacing:1px;color:#9aa3bb}
</style>
</head>
<body>
<div class="topbar">
  <div>Welcome visitor you can <a href="#">Login</a> or <a href="#">Create an account</a></div>
  <div class="account-links"><span>♥ Wishlist (0)</span><span>My Account</span><span>Checkout</span><span>Cart (0)</span></div>
</div>
<header class="site-header"><div class="brand">LINEN LARDER</div></header>
<nav class="main-nav">
  <a href="#">HOME</a><a href="#" class="active">OUR PRODUCTS</a><a href="#">ABOUT US</a><a href="#">CONTACT US</a><a href="#">FAQ</a>
</nav>

<section class="hero">
  <div class="hero-image" role="img" aria-label="Folded colourful kitchen towels and tea towels stacked together"></div>
  <div class="hero-labels"><span>Kitchen Towels</span><span>Dish Cloths</span><span>Tea Towels</span></div>
</section>
<div class="hero-arrow prev"><svg width="10" height="14"><path d="M8 1 2 7l6 6" stroke="#fff" stroke-width="2" fill="none"/></svg></div>
<div class="hero-arrow next"><svg width="10" height="14"><path d="M2 1l6 6-6 6" stroke="#fff" stroke-width="2" fill="none"/></svg></div>
<div class="hero-dots"><i></i><i></i><i class="on"></i><i></i></div>

<h2 class="section-title featured-title">FEATURED PRODUCTS</h2>
<div class="category-list">
  <div class="category"><div class="swatch" role="img" aria-label="Checked dish cloths fanned out" style="background:linear-gradient(90deg,#d9c9e6,#f0e3c4,#e6b8c8)"></div><div class="label">DISH CLOTHS<svg width="14" height="28"><path d="M0 0 14 14 0 28Z" fill="#fff"/></svg></div></div>
  <div class="category"><div class="swatch" role="img" aria-label="Striped kitchen towels laid flat" style="background:linear-gradient(90deg,#e8d9b8,#cfd8e6,#e9e2d4)"></div><div class="label">KITCHEN TOWELS<svg width="14" height="28"><path d="M0 0 14 14 0 28Z" fill="#fff"/></svg></div></div>
  <div class="category"><div class="swatch" role="img" aria-label="Bright tea towels in red and blue" style="background:linear-gradient(90deg,#d74848,#e9e4de,#4a7fc1)"></div><div class="label">TEA TOWELS<svg width="14" height="28"><path d="M0 0 14 14 0 28Z" fill="#fff"/></svg></div></div>
</div>
<div class="feature-image" role="img" aria-label="Printed tea towels hanging on a line with a best product seller caption"></div>

<section class="welcome">
  <h2>WELCOME TO LINEN LARDER</h2>
  <p>Lorem ipsum dolor sit amet, consectetur adipiscing elit. Proin nisl auctor justo, aliquam sed volutpat. Mauris dui erat, tempus et molestie nec, pulvinar sed dolor. Aenean sollicitudin pharetra ultrices. Quisque ac diam id erat finibus pretium. Nunc blandit arcu vitae felis vehicula tincidunt.</p>
  <p>Donec ornare tristique justo. Nullam volutpat lacus euismod fermentum at. Etiam placerat lectus. Praesent ut tortor porta, aliquet libero ac, porttitor nunc. Curabitur eget lorem at quam vulputate pretium. Vivamus quis magna sed neque cursus ultrices. Sed vitae magna nec libero eleifend vulputate sit amet in tellus.</p>
  <a class="btn" href="#">READ MORE</a>
</section>
<section class="testimonials">
  <h2>CLIENTS SPEAK</h2>
  <div class="quote">Lorem ipsum dolor sit amet, consectetur adipiscing elit. Integer facilisis libero mauris, at molestie justo dictum vel. Mauris tempor tellus nec lacus, quis vehicula odio luctus sit amet.</div>
  <div class="author"><div class="avatar" role="img" aria-label="Client portrait"></div><div><b>Margot</b>Store Owner</div></div>
</section>

<div class="brands">
  <span><i></i>Harlow &amp; Co</span><span><i></i>Northmere</span><span><i></i>Rosemont</span><span><i></i>Linenly</span><span><i></i>Fernbrook</span>
</div>

<footer class="site-footer">
  <div class="footer-cols">
    <div class="footer-col"><h3>Useful Links</h3><div class="twin"><ul><li>Home</li><li>About Us</li><li>Products</li><li>Contact Us</li></ul><ul><li>FAQ</li><li>Delivery</li><li>Returns</li><li>Privacy Policy</li></ul></div></div>
    <div class="footer-col"><h3>Products</h3><ul><li>Tea Towels</li><li>Kitchen Towels</li><li>Dish Cloths</li><li>Gift Packs</li></ul></div>
    <div class="footer-col"><h3>Contact Info</h3><ul><li><svg width="8" height="10"><path d="M4 0a3.5 3.5 0 0 1 3.5 3.5C7.5 6 4 10 4 10S.5 6 .5 3.5A3.5 3.5 0 0 1 4 0z" fill="#8f9ab6"/></svg>12 Linen Lane, Harbourtown</li><li><svg width="8" height="10"><rect x="1" y="0" width="6" height="10" rx="1.5" fill="#8f9ab6"/></svg>+00 123 456 789</li><li><svg width="9" height="7"><rect width="9" height="7" fill="#8f9ab6"/><path d="M0 0l4.5 4L9 0" stroke="#2b3552" fill="none"/></svg>hello@linenlarder.example</li></ul></div>
    <div class="footer-col"><h3>Follow Us</h3><ul><li><span class="dot"></span>Social one</li><li><span class="dot"></span>Social two</li><li><span class="dot"></span>Social three</li></ul></div>
  </div>
</footer>
<div class="copyright"><span class="mark">LINEN LARDER</span><span>Copyright 2015 Linen Larder. All rights reserved.</span></div>
</body>
</html>
```